Creative Businesss Card desgin!

Create a business card for our business Gleam window cleaning!
We are open to creative ideas as long as it maintains a professional image.

Target Market(s)

Small Commercial window cleaning clients including car dealerships, strata manager, cafe

Industry/Entity Type

Window Cleaning

Contact Information for Business Card

Daniel Prescott
General Manager
Gleam Window Cleaning

daniel@gleamservices.com.au
pane-care-southbank.com.au
Ph: 1800 GET GLEAM
Mob: 0437 582 061

Colors
fbed22
0392cd

Requirements
Should not have
• Stock window cleaning/ squeegee graphics

```html
<!DOCTYPE html>
<html lang="en">
<head>
<meta charset="utf-8">
<title>Gleam Window Cleaning – Business Card</title>
<link href="https://fonts.googleapis.com/css2?family=Arimo:wght@400;700&display=swap" rel="stylesheet">
<style>
  :root {
    --bg: #2b2b2b;
    --blue: #14679f;
    --blue-ink: #0d4f86;
    --yellow: #f2e72c;
    --line: #1a1a1a;
  }
  * { box-sizing: border-box; margin: 0; padding: 0; }
  html, body { width: 1200px; height: 997px; overflow: hidden; background: var(--bg); }
  body { position: relative; font-family: "Arimo", Arial, sans-serif; }

  .card {
    position: absolute;
    border-radius: 22px;
    overflow: hidden;
    background: var(--blue);
    box-shadow: 0 10px 30px rgba(0,0,0,.5);
  }
  .card-split { position: absolute; inset: 0; width: 100%; height: 100%; }

  /* Back card */
  .card-back { left: 70px; top: 80px; width: 560px; height: 340px; }
  .card-back .brand { position: absolute; left: 44px; top: 70px; color: var(--yellow); font-weight: 700; }
  .brand-name { font-size: 54px; letter-spacing: 2px; line-height: 1; }
  .brand-sub { font-size: 20px; letter-spacing: 1px; margin-top: 4px; }
  .address { position: absolute; left: 120px; top: 180px; color: var(--yellow); font-size: 16px; line-height: 1.4; }
  .quote-btn {
    position: absolute; left: 120px; top: 252px;
    background: var(--yellow); color: var(--blue-ink);
    font-size: 14px; padding: 7px 14px; border-radius: 4px;
  }
  .services { position: absolute; left: 400px; top: 70px; list-style: none; color: var(--blue-ink); font-size: 15px; line-height: 1.45; }

  /* Front card */
  .card-front { left: 520px; top: 500px; width: 620px; height: 378px; }
  .card-front .brand { position: absolute; left: 40px; top: 64px; color: var(--yellow); font-weight: 700; }
  .card-front .brand-name { font-size: 64px; }
  .card-front .brand-sub { font-size: 24px; }
  .contacts { position: absolute; left: 40px; top: 226px; list-style: none; color: #fff; font-size: 17px; }
  .contacts li { display: flex; align-items: center; gap: 12px; height: 28px; }
  .contact-icon { width: 18px; height: 18px; flex: none; }
  .person { position: absolute; right: 28px; top: 244px; text-align: right; color: var(--blue-ink); }
  .person-name { font-size: 20px; font-weight: 700; }
  .person-title { font-size: 15px; margin-top: 4px; }
</style>
</head>
<body>

<section class="card card-back" aria-label="Business card, back">
  <svg class="card-split" viewBox="0 0 560 340" preserveAspectRatio="none" aria-hidden="true">
    <polygon points="330,0 560,0 560,340 380,340" fill="var(--yellow)" stroke="var(--line)" stroke-width="1"/>
  </svg>
  <div class="brand">
    <div class="brand-name">GLEAM</div>
    <div class="brand-sub">WINDOW CLEANING</div>
  </div>
  <p class="address">1204/88 Harbour Rd<br>Southbank VIC 3006</p>
  <span class="quote-btn">Get a Free Quote Today »</span>
  <ul class="services">
    <li>Our Services</li>
    <li>Window Cleaning</li>
    <li>Pressure Cleaning</li>
    <li>Gutter Cleaning</li>
    <li>Graffiti Removal</li>
  </ul>
</section>

<section class="card card-front" aria-label="Business card, front">
  <svg class="card-split" viewBox="0 0 620 378" preserveAspectRatio="none" aria-hidden="true">
    <polygon points="370,0 620,0 620,378 420,378" fill="var(--yellow)" stroke="var(--line)" stroke-width="1"/>
  </svg>
  <div class="brand">
    <div class="brand-name">GLEAM</div>
    <div class="brand-sub">WINDOW CLEANING</div>
  </div>
  <ul class="contacts">
    <li>
      <svg class="contact-icon" viewBox="0 0 18 18" aria-hidden="true"><circle cx="9" cy="9" r="9" fill="var(--yellow)"/><rect x="6" y="4" width="6" height="10" rx="1" fill="var(--blue)"/></svg>
      0437 582 061
    </li>
    <li>
      <svg class="contact-icon" viewBox="0 0 18 18" aria-hidden="true"><circle cx="9" cy="9" r="9" fill="var(--yellow)"/><path d="M5 6 Q9 3 13 6 L12 8 L10 7 L8 7 L6 8 Z M5 10 H13 V13 H5 Z" fill="var(--blue)"/></svg>
      1800 GET GLEAM
    </li>
    <li>
      <svg class="contact-icon" viewBox="0 0 18 18" aria-hidden="true"><circle cx="9" cy="9" r="9" fill="var(--yellow)"/><rect x="4.5" y="5.5" width="9" height="7" fill="var(--blue)"/><path d="M4.5 5.5 L9 9.5 L13.5 5.5" stroke="var(--yellow)" fill="none"/></svg>
      daniel@gleamservices.com.au
    </li>
    <li>
      <svg class="contact-icon" viewBox="0 0 18 18" aria-hidden="true"><circle cx="9" cy="9" r="9" fill="var(--yellow)"/><circle cx="9" cy="9" r="5" fill="none" stroke="var(--blue)" stroke-width="1.4"/><path d="M4 9 H14 M9 4 V14" stroke="var(--blue)" stroke-width="1.2"/></svg>
      pane-care-southbank.com.au
    </li>
  </ul>
  <div class="person">
    <div class="person-name">Daniel Prescott</div>
    <div class="person-title">General Manager</div>
  </div>
</section>

</body>
</html>
```